Website design for new health & wellness company

We need our website to be designed in a user friendly way. Needs to be aesthetically pleasing to viewer and easy to navigate and upload content for our small team . The logo should be completely redesigned , please do not reference the current one thats on our site for a starting place. (included below though) We want to move away from that.

the website is : www.brightpathmoments.net

We are a small group of writers/coaches who believe that to change the world you have to be the change and we provide tips/suggestions for every day life that if followed can make a huge difference in your life and overall being.

Target Market(s)

Men and women ages 22 to 50

Industry/Entity Type

Health And Wellness

Logo Text

Cultivate the life of your dreams

Coding

Coded - Design and coding required

Number of Pages Required

3 page

Font styles to use
Sans Serif

Colors

Designer to choose colors to be used in the design.

Requirements
Must have
• Easy to navigate. Mobile friendly. Gender neutral, should appeal to both.

```html
<!DOCTYPE html>
<html lang="en">
<head>
<meta charset="utf-8">
<title>Bright Path Moments</title>
<link href="https://fonts.googleapis.com/css2?family=Poppins:wght@300;400;500;600&family=Dancing+Script:wght@500;700&display=swap" rel="stylesheet">
<style>
:root{
  --green:#8dc63f;
  --green-dark:#76ad2c;
  --ink:#2b2b2b;
  --text:#6d6d6d;
  --muted:#9a9a9a;
  --line:#e4e4e4;
  --light:#f2f2f2;
  --dark:#1f2225;
  --white:#ffffff;
}
*{box-sizing:border-box;margin:0;padding:0}
html,body{width:1200px;height:3758px;overflow:hidden}
body{font-family:'Poppins',sans-serif;color:var(--text);background:var(--white);position:relative;font-size:13px}
section,header,footer,.topbar{position:absolute;left:0;width:1200px}
.abs{position:absolute}
.script{font-family:'Dancing Script',cursive;font-weight:700}
.btn-green{position:absolute;background:var(--green);color:var(--white);font-size:12px;font-weight:500;display:flex;align-items:center;justify-content:center;gap:6px;border-radius:2px}
.dot{width:7px;height:7px;border-radius:50%;background:currentColor;display:inline-block}

/* top bar */
.topbar{top:0;height:45px;border-top:4px solid var(--green);border-bottom:1px solid var(--line);font-size:12px;color:var(--ink)}
.topbar .contact{left:155px;top:11px;display:flex;gap:24px}
.topbar .contact span{display:flex;align-items:center;gap:6px}
.topbar .social{right:155px;top:13px;display:flex;gap:10px;align-items:center}
.topbar .social i{width:9px;height:9px;border-radius:50%;background:var(--green);display:block}
.topbar .social b{width:1px;height:10px;background:var(--line);display:block}

/* header */
header{top:45px;height:75px}
.brand{left:155px;top:18px;display:flex;align-items:center;gap:8px}
.brand-name{font-size:18px;font-weight:600;color:var(--ink);line-height:1}
.brand-mark{width:14px;height:14px;border-radius:50%;background:var(--green)}
.nav{right:155px;top:26px;display:flex;gap:30px;font-size:13px;color:var(--ink)}
.nav .active{color:var(--green)}

/* hero */
.hero{top:120px;height:481px;background:linear-gradient(100deg,#5e6a3a 0%,#7a7f4a 35%,#8a7a55 60%,#6b5a63 80%,#4c4a3c 100%)}
.hero-title{left:155px;top:140px;font-size:50px;color:var(--white)}
.hero-title em{font-style:normal;color:var(--green)}
.hero-sub{left:155px;top:222px;width:360px;font-size:13px;line-height:20px;color:var(--white)}
.hero .btn-green{left:155px;top:296px;width:128px;height:34px}
.hero-arrows{left:155px;top:426px;display:flex;gap:18px}

/* welcome */
.welcome{top:601px;height:321px}
.welcome-photo{left:155px;top:0;width:356px;height:321px;background:linear-gradient(135deg,#d8dde3,#6b7f96 60%,#3a4250)}
.welcome-title{left:584px;top:66px;font-size:36px;color:var(--ink)}
.welcome-title em{font-style:normal;color:var(--green)}
.welcome-text{left:584px;top:130px;width:460px;font-size:12px;line-height:20px}
.btn-outline{position:absolute;left:586px;top:210px;width:130px;height:36px;border:2px solid var(--ink);color:var(--ink);font-size:12px;font-weight:500;display:flex;align-items:center;justify-content:center;gap:6px}

/* section title */
.sec-title{left:0;width:1200px;display:flex;align-items:center;justify-content:center;gap:22px;font-size:34px;color:var(--ink)}
.sec-title em{font-style:normal;color:var(--green)}
.sec-title .rule{display:flex;align-items:center;gap:0}
.sec-title .rule i{width:80px;height:2px;background:var(--muted);display:block}
.sec-title .rule b{width:8px;height:8px;border:2px solid var(--muted);border-radius:50%;display:block}

/* tips */
.tips{top:922px;height:511px;background:var(--light)}
.tips .sec-title{top:55px}
.tip-row{left:155px;top:130px;display:flex;gap:25px}
.tip{width:203px;height:316px;background:var(--white)}
.tip.featured{box-shadow:0 4px 14px rgba(0,0,0,.15)}
.tip-photo{height:135px}
.tip h3{font-size:12px;font-weight:600;color:var(--ink);margin:24px 16px 0;line-height:17px;height:34px}
.tip.featured h3{color:var(--green)}
.tip p{font-size:11px;line-height:17px;margin:12px 16px 0;height:52px}
.tip .more{font-size:11px;font-weight:600;color:var(--green);margin:26px 16px 0;display:flex;align-items:center;gap:6px}
.tip-arrow{top:280px}

/* reviews */
.reviews{top:1433px;height:1343px}
.reviews .sec-title{top:60px}
.post-title{font-size:18px;font-weight:500;color:var(--ink)}
.post-small .post-title{font-size:14px}
.meta{font-size:11px;color:var(--muted)}
.meta em{font-style:normal;color:var(--green)}
.excerpt{font-size:11px;line-height:17px}
.stats{font-size:11px;color:var(--muted);display:flex;gap:10px;align-items:center}
.stats span{display:flex;align-items:center;gap:4px}
.post-main{left:155px;top:140px;width:586px}
.post-small{top:746px;width:283px}
.panel{position:absolute;background:var(--white);border:1px solid var(--line);box-shadow:0 2px 8px rgba(0,0,0,.08)}
.panel h4{font-family:'Dancing Script',cursive;font-weight:700;font-size:26px;color:var(--ink);text-align:center;padding-top:22px}
.panel h4::after{content:"";display:block;width:100px;height:1px;background:var(--line);margin:8px auto 0}
.cat-list{list-style:none;margin:18px 20px 0}
.cat-list li{display:flex;justify-content:space-between;font-size:11px;color:var(--ink);height:38px;align-items:center;border-bottom:1px solid var(--line)}
.cat-list li.active{color:var(--green)}
.pop-list{margin:20px 20px 0}
.pop{display:flex;gap:14px;height:93px}
.pop .thumb{width:70px;height:72px;flex:none}
.pop p{font-size:11px;line-height:16px;color:var(--ink)}
.pop .likes{font-size:10px;color:var(--green);margin-top:6px;display:flex;align-items:center;gap:4px}
.promo{left:764px;top:1027px;width:281px;height:248px;background:linear-gradient(135deg,#9fd14e,#7bb33a 60%,#4d6e2a)}
.promo .ring{position:absolute;left:118px;top:102px;width:44px;height:44px;border:2px solid rgba(255,255,255,.8);border-radius:50%}

/* coaching */
.coaching{top:2776px;height:471px;background:var(--light)}
.coach-panel{left:0;top:0;width:599px;height:471px;background:linear-gradient(90deg,#3a3a3a,#555 55%,#6b6b6b)}
.coach-photo{left:340px;top:0;width:200px;height:471px;background:linear-gradient(180deg,#7a6a5e,#4d4540 70%,#3d3835)}
.coach-title{left:155px;top:125px;font-size:28px;font-weight:500;color:var(--white);line-height:34px}
.coach-title em{font-style:normal;color:var(--green)}
.coach-text{left:155px;top:205px;width:230px;font-size:13px;line-height:20px;color:#e0e0e0}
.coaching .btn-green{left:155px;top:267px;width:128px;height:34px}
.stat{position:absolute;width:180px}
.stat .num{font-size:46px;font-weight:300;color:var(--green);line-height:1}
.stat .lbl{font-size:13px;color:var(--ink);line-height:18px;margin-top:18px;letter-spacing:.5px}

/* footer */
footer{top:3311px;height:447px;background:linear-gradient(180deg,#1d2023,#26292c 50%,#1b1d1f);color:#cfcfcf}
.nl-kicker{top:62px;width:1200px;text-align:center;font-size:11px;letter-spacing:1px}
.nl-title{top:82px;width:1200px;text-align:center;font-size:26px;font-weight:600;color:var(--white);letter-spacing:1px}
.nl-sub{top:120px;width:1200px;text-align:center;font-size:13px}
.nl-rule{left:580px;top:148px;width:40px;height:2px;background:var(--white)}
.nl-form{left:433px;top:189px;width:334px;height:30px;display:flex}
.nl-form .field{flex:1;background:var(--white);color:var(--ink);font-size:11px;padding-left:12px;display:flex;align-items:center}
.nl-form .send{width:46px;background:var(--green);display:flex;align-items:center;justify-content:center}
.follow{top:246px;width:1200px;text-align:center;font-size:15px;color:var(--white)}
.follow-icons{left:548px;top:277px;display:flex;gap:12px}
.follow-icons i{width:22px;height:22px;border:1px solid var(--white);border-radius:50%;display:block;position:relative}
.follow-icons i::after{content:"";position:absolute;left:7px;top:7px;width:6px;height:6px;border-radius:50%;background:var(--white)}
.follow-icons i.on{background:var(--green);border-color:var(--green)}
.addr{left:155px;top:262px;font-size:12px;line-height:20px}
.addr strong{color:var(--green);font-weight:600;display:flex;align-items:center;gap:6px}
.help{right:155px;top:262px;font-size:12px;line-height:20px;text-align:right}
.help u{color:var(--white)}
.foot-rule{left:155px;top:361px;width:890px;height:1px;background:#3c3f42}
.copy{left:155px;top:383px;font-size:11px}
.copy strong{color:var(--green);font-weight:600}
.to-top{left:1020px;top:380px}
</style>
</head>
<body>

<div class="topbar">
  <div class="abs contact">
    <span><svg width="11" height="11" viewBox="0 0 24 24"><path d="M6.6 10.8a15 15 0 0 0 6.6 6.6l2.2-2.2a1 1 0 0 1 1-.25 11 11 0 0 0 3.6.6 1 1 0 0 1 1 1V20a1 1 0 0 1-1 1A17 17 0 0 1 3 4a1 1 0 0 1 1-1h3.5a1 1 0 0 1 1 1 11 11 0 0 0 .6 3.6 1 1 0 0 1-.25 1z" fill="#8dc63f"/></svg>(310) 555-0142</span>
    <span><svg width="12" height="10" viewBox="0 0 24 18"><rect x="1" y="1" width="22" height="16" fill="none" stroke="#8dc63f" stroke-width="2"/><path d="M1 1l11 9 11-9" fill="none" stroke="#8dc63f" stroke-width="2"/></svg>info@brightpathmoments.net</span>
  </div>
  <div class="abs social"><i></i><b></b><i></i><b></b><i></i><b></b><i></i></div>
</div>

<header>
  <div class="abs brand"><span class="brand-name">Bright Path</span><span class="brand-mark"></span></div>
  <nav class="abs nav"><span class="active">Home</span><span>About Us</span><span>Change Your Life</span><span>Services</span><span>Blog</span><span>Contact Us</span></nav>
</header>

<section class="hero">
  <div class="abs" role="img" aria-label="Photo of a woman running outdoors on a sunlit path" style="inset:0"></div>
  <h1 class="abs hero-title script">Train Your <em>Inspiration</em></h1>
  <p class="abs hero-sub">Enthusiastically evolve low-risk high-yield content rather than process-centric benefits</p>
  <a class="btn-green">Contact Now <span class="dot"></span></a>
  <div class="abs hero-arrows">
    <svg width="22" height="14" viewBox="0 0 22 14"><path d="M21 7H2M7 1L1 7l6 6" fill="none" stroke="#8dc63f" stroke-width="2"/></svg>
    <svg width="22" height="14" viewBox="0 0 22 14"><path d="M1 7h19M15 1l6 6-6 6" fill="none" stroke="#fff" stroke-width="2"/></svg>
  </div>
</section>

<section class="welcome">
  <div class="abs welcome-photo" role="img" aria-label="Photo of a coach speaking at a lectern"></div>
  <h2 class="abs welcome-title script">Welcome to <em>Bright Path Moments</em></h2>
  <p class="abs welcome-text">Lorem ipsum dolor sit amet, consetetur sadipscing elitr, sed diam nonumy eirmod tempor invidunt ut labore et dolore magna aliquyam erat, sed diam voluptua. At vero eos et accusam ...</p>
  <a class="btn-outline">Know More <span class="dot"></span></a>
</section>

<section class="tips">
  <h2 class="abs sec-title script"><span class="rule"><i></i><b></b></span><span>Latest <em>Tips</em></span><span class="rule"><b></b><i></i></span></h2>
  <svg class="abs tip-arrow" style="left:104px" width="20" height="12" viewBox="0 0 20 12"><path d="M19 6H2M6 1L1 6l5 5" fill="none" stroke="#8dc63f" stroke-width="2"/></svg>
  <div class="abs tip-row">
    <article class="tip"><div class="tip-photo" role="img" aria-label="Photo of a group doing yoga stretches" style="background:linear-gradient(135deg,#e9e4dc,#c9bfb3)"></div><h3>How To Stay Fit</h3><p>There are many variations of passages of Lorem Ipsum available, but the majority have...</p><div class="more">Read More <span class="dot"></span></div></article>
    <article class="tip featured"><div class="tip-photo" role="img" aria-label="Photo of a family cooking healthy food together" style="background:linear-gradient(135deg,#d9c7a8,#8f9a4e)"></div><h3>Information For Cooking Together</h3><p>There are many variations of passages of Lorem Ipsum available, but the majority have suffered...</p><div class="more">Read More <span class="dot"></span></div></article>
    <article class="tip"><div class="tip-photo" role="img" aria-label="Photo of a person stretching by the sea" style="background:linear-gradient(180deg,#8fb3d4,#3f6f92 60%,#2e4d5e)"></div><h3>Suggestions for Stay Healthy</h3><p>There are many variations of passages of Lorem Ipsum available, but the majority have...</p><div class="more">Read More <span class="dot"></span></div></article>
    <article class="tip"><div class="tip-photo" role="img" aria-label="Photo of a group exercising on a beach" style="background:linear-gradient(180deg,#9ec7e8,#5b8fbf 60%,#c9b48a)"></div><h3>Tips For Getting Started</h3><p>There are many variations of passages of Lorem Ipsum available, but the majority have suffered...</p><div class="more">Read More <span class="dot"></span></div></article>
  </div>
  <svg class="abs tip-arrow" style="left:1072px" width="20" height="12" viewBox="0 0 20 12"><path d="M1 6h17M14 1l5 5-5 5" fill="none" stroke="#2b2b2b" stroke-width="2"/></svg>
</section>

<section class="reviews">
  <h2 class="abs sec-title script"><span class="rule"><i></i><b></b></span><span>Our <em>Reviews</em></span><span class="rule"><b></b><i></i></span></h2>

  <article class="abs post-main">
    <h3 class="post-title">Stretching is Important!</h3>
    <div class="meta" style="margin-top:18px">By Maren Holt / <em>December 5, 2017</em></div>
    <div role="img" aria-label="Photo of a woman stretching on a park path" style="margin-top:16px;height:318px;background:linear-gradient(135deg,#c9b46a,#8a8f3c 45%,#5d6e2e 80%)"></div>
    <p class="excerpt" style="margin-top:22px">one of the best Hartwell book, forsook emptied much indecisively angelfish as less flew some for boyish post up in this like, ethereally flailed. From multiply form waters had midst moving is also deep wild. Signs saying him also void.</p>
    <div style="display:flex;justify-content:space-between;align-items:center;margin-top:24px">
      <span class="btn-green" style="position:static;width:130px;height:35px">Read More <span class="dot"></span></span>
      <div class="stats">
        <span><svg width="11" height="10" viewBox="0 0 12 10"><path d="M1 1h10v6H5L2 9V7H1z" fill="none" stroke="#9a9a9a"/></svg>05 Comments</span>|
        <span><svg width="11" height="10" viewBox="0 0 12 10"><path d="M6 9L1.5 4.5a2.3 2.3 0 0 1 4.5-2 2.3 2.3 0 0 1 4.5 2z" fill="none" stroke="#9a9a9a"/></svg>62 Likes</span>| <span>Share</span>
      </div>
    </div>
  </article>

  <article class="abs post-small" style="left:155px">
    <h3 class="post-title">Inspirational fitness quotes</h3>
    <div class="meta" style="margin-top:22px">By Maren Holt / <em>September 5, 2017</em></div>
    <div role="img" aria-label="Photo of a trainer guiding a lunge in a gym" style="margin-top:12px;height:281px;background:linear-gradient(135deg,#6b6b6b,#b9b2a8 50%,#4a4a4a)"></div>
    <p class="excerpt" style="margin-top:17px">one of the best Hartwell book, forsook emptied much indecisively angelfish as less flew some for boyish post up in...</p>
    <span class="btn-green" style="position:static;width:95px;height:33px;margin-top:30px">Read More <span class="dot"></span></span>
    <div class="stats" style="margin-top:13px"><span>05 Comments</span>| <span>62 Likes</span>| <span>Share</span></div>
    <div style="height:1px;background:var(--line);margin-top:12px"></div>
  </article>

  <article class="abs post-small" style="left:458px">
    <h3 class="post-title">Inspirational fitness quotes</h3>
    <div class="meta" style="margin-top:22px">By Maren Holt / <em>September 5, 2017</em></div>
    <div role="img" aria-label="Photo of a woman doing a floor exercise in a gym" style="margin-top:12px;height:281px;background:linear-gradient(135deg,#8a8a8a,#d0cbc4 50%,#5a5a5a)"></div>
    <p class="excerpt" style="margin-top:17px">one of the best Hartwell book, forsook emptied much indecisively angelfish as less flew some for boyish post up in...</p>
    <span class="btn-green" style="position:static;width:95px;height:33px;margin-top:30px">Read More <span class="dot"></span></span>
    <div class="stats" style="margin-top:13px"><span>05 Comments</span>| <span>62 Likes</span>| <span>Share</span></div>
    <div style="height:1px;background:var(--line);margin-top:12px"></div>
  </article>

  <aside class="panel" style="left:764px;top:128px;width:281px;height:370px">
    <h4>Categories</h4>
    <ul class="cat-list">
      <li><span>Aqua Fitness</span><span>(06)</span></li>
      <li><span>Dancing</span><span>(03)</span></li>
      <li><span>Fitness</span><span>(26)</span></li>
      <li class="active"><span>Meditation</span><span>(07)</span></li>
      <li><span>Yoga</span><span>(08)</span></li>
      <li><span>Inspirations</span><span>(02)</span></li>
      <li><span>Outdoors</span><span>(06)</span></li>
    </ul>
  </aside>

  <aside class="panel" style="left:764px;top:513px;width:281px;height:474px">
    <h4>Most Popular</h4>
    <div class="pop-list">
      <div class="pop"><div class="thumb" role="img" aria-label="Photo of a workout class" style="background:linear-gradient(135deg,#b0a89c,#5f5a55)"></div><div><p>Contrary to popular belief, Lorem Ipsum...</p><div class="likes">&#9825; 62 Likes</div></div></div>
      <div class="pop"><div class="thumb" role="img" aria-label="Photo of people training together" style="background:linear-gradient(135deg,#c7b9a6,#6e5f56)"></div><div><p>All the Lorem Ipsum generators Internet...</p><div class="likes">&#9825; 17 Likes</div></div></div>
      <div class="pop"><div class="thumb" role="img" aria-label="Photo of an outdoor fitness session" style="background:linear-gradient(135deg,#d8c79a,#8a7a4e)"></div><div><p>The generated Lorem Ipsum is therefore...</p><div class="likes">&#9825; 23 Likes</div></div></div>
      <div class="pop"><div class="thumb" role="img" aria-label="Photo of a stretching exercise" style="background:linear-gradient(135deg,#e0d4cc,#9a8a82)"></div><div><p>Tobias Wren, Latin professor at Brookvale...</p><div class="likes">&#9825; 56 Likes</div></div></div>
    </div>
  </aside>

  <div class="abs promo" role="img" aria-label="Photo of running shoes with a green overlay"><span class="ring"></span></div>
</section>

<section class="coaching">
  <div class="abs coach-panel"></div>
  <div class="abs coach-photo" role="img" aria-label="Photo of a fit woman standing confidently"></div>
  <h2 class="abs coach-title"><em>LIFE</em> COACHING<br>BENEFITS</h2>
  <p class="abs coach-text">Learn the skills you'll need to promote and run business</p>
  <a class="btn-green">Learn More <span class="dot"></span></a>
  <div class="stat" style="left:679px;top:90px"><div class="num">480</div><div class="lbl">TOTAL PEOPLE TRAINED IN OUR ORGANAIZATION</div></div>
  <div class="stat" style="left:872px;top:90px"><div class="num">009</div><div class="lbl">DIFFERENT COACHES TAKING CARE OF YOU</div></div>
  <div class="stat" style="left:679px;top:287px"><div class="num">24</div><div class="lbl">HOURS A DAY OPENED FOR YOUR TRAININGS</div></div>
  <div class="stat" style="left:872px;top:287px"><div class="num">100</div><div class="lbl">PERCENT SATISFACTION GUARANTEED</div></div>
</section>

<footer>
  <div class="abs" role="img" aria-label="Dim photo of a gym interior" style="inset:0;opacity:.4;background:linear-gradient(120deg,transparent,#3a3d40 50%,transparent)"></div>
  <p class="abs nl-kicker">JOIN BRIGHT PATH MOMENTS</p>
  <h2 class="abs nl-title">NEWSLETTER</h2>
  <p class="abs nl-sub">Subscribe to our newsletter to get latest scoop right to your inbox.</p>
  <div class="abs nl-rule"></div>
  <div class="abs nl-form"><span class="field">Enter Your Email ...</span><span class="send"><svg width="13" height="12" viewBox="0 0 14 12"><path d="M0 0l14 6-14 6 2-6z" fill="#fff"/></svg></span></div>
  <p class="abs follow">Follow Us</p>
  <div class="abs follow-icons"><i></i><i class="on"></i><i></i><i></i></div>
  <div class="abs addr"><strong><svg width="9" height="12" viewBox="0 0 10 14"><path d="M5 0a5 5 0 0 0-5 5c0 4 5 9 5 9s5-5 5-9a5 5 0 0 0-5-5zm0 7a2 2 0 1 1 0-4 2 2 0 0 1 0 4z" fill="#8dc63f"/></svg>BRIGHT PATH MOMENTS</strong>Box 41870 Harlow Bay, Lindmere</div>
  <div class="abs help">Need help? Call Us: <svg width="10" height="10" viewBox="0 0 24 24"><path d="M6.6 10.8a15 15 0 0 0 6.6 6.6l2.2-2.2a1 1 0 0 1 1-.25 11 11 0 0 0 3.6.6 1 1 0 0 1 1 1V20a1 1 0 0 1-1 1A17 17 0 0 1 3 4a1 1 0 0 1 1-1h3.5a1 1 0 0 1 1 1 11 11 0 0 0 .6 3.6 1 1 0 0 1-.25 1z" fill="#fff"/></svg> +12-34-55 01 42<br><u>info@brightpathmoments.net</u></div>
  <div class="abs foot-rule"></div>
  <p class="abs copy">© 2017 <strong>BRIGHT PATH MOMENTS</strong>. All Rights Reserved.</p>
  <svg class="abs to-top" width="16" height="18" viewBox="0 0 16 18"><path d="M8 0l8 9h-5v9H5V9H0z" fill="#8dc63f"/></svg>
</footer>

</body>
</html>
```